A live music performing company website

Hello guys!

We provide live music performance at wedding parties, business exhibitions, and dinner parties. We have three performing teams, a classic music team, a Jazz music team, and a pop music team, in the company.

We already have a logo. Now we are looking for a website proposal which should fin in with the logo and our company style. What we intend to represent is professional, elegant, and luxury atmosphere in the web design.

== Here is the spec ==

* The IA(Information Architecture) of the site will be ("Home" is the root node, "-" is the first sub-layer, "+" is the second sub-layer):

Home
- Groups(brief intro)
+Classic (detail intro)
+Jazz (detail intro)
+Pop (detail intro)
- Members
- Videos
+ Classic
+ Jazz
+ Pop
- Pricing
- Order

*One home page.

*Several internal pages:
- One is used to brief the three performing groups. ("Groups" in the IA)
++ Three pages(or tags) to introduce each groups.
- One is for introducing our primary members ("Members" in the iA)
- One is MV sharing for each performing group. ("Videos" in the IA)
- One is for introducing our pricing packages. ("Pricing" in the IA)
- One is for making order (holds a html form). ("Order" in the IA)
- One is for usual intro pages, such as "contact us", "about us", "Jobs" ...

=== Update 2011/08/29 ===
We also need a theme for our Blog, you can assume it hosts by Pindle.

The theme has to represent the same atmosphere with the main site.
======
Updates

We just add a requirement in the "overview" section. We need a theme for your blog system. We have raised our budget from to 400, and add 2 participation payment.

Thanks!!

Just uploaded a .pdf, which includes our company name and slogan. The logo has been uploaded as an .ai file yesterday.

We have added a requirement in the "Must Have Priorities", which is about the home page.

We have added a "Nice to Have Priorities", which is about a "Chatterly Like box" element on the home page.

Please check it up. Thanks!!!

About the "Photo slider", we prefer the sixth and seventh one in this page.

http://codeleafhub.mintgrove.net/web-programming/47-javascript/85-30-best-dommix-photo-plugins-sliders-slideshow-galleries-and-scrollers.html

Target Market(s)

*People who are going to get married in the near future.

*People who are going to launch a dinner party.

*Business people who are going to raise an exhibition.

Industry/Entity Type

Wedding

Requirements
Must have
• *Home page:
+ An area will be used to put a photo slider to show our recent performances.
+ Must be arranged at the resolution of 960px * 600px.
+ Has to present the company name, the logo, and the slogan. How to arrange all of them is up to designer. (Company name and slogan are written in Chinese, they are saved in the pdf as an attachment file.)

*Internal pages:
+ The width of internal pages has to be 960px.

* "Videos" page:
+ Has the capability to arrange the videos by:
- Date (Default arrangement)
- Geo location (With a Terrova map, once our customers click on the pin, the web page could show a list of recording at the location.)
- Category (Biz exhibitions, wedding parties, or dinner parties)
Nice to have
• * Designers can use the preview photos(with watermark) on Picturbarn.com. We can go to purchase the legal usage once your design has been accepted.

* If it's possible to embed a "Chatterly Like box" (Please reference it at: http://developers.chatterly.net/docs/reference/plugins/like-box/) on the home page, it will be great. But if the box might threat the integrity of the page, then don't use it.
Should not have
• * No Flash.
* No tech coding.

```html
<!DOCTYPE html>
<html lang="zh-Hant">
<head>
<meta charset="utf-8">
<title>悅聲藝術 — Wedding music</title>
<link rel="stylesheet" href="https://fonts.googleapis.com/css2?family=Arimo:wght@400;700&family=Noto+Sans+TC:wght@400&family=Roboto+Condensed:wght@300;400&display=swap">
<style>
  :root {
    --canvas: #e6e6e6;
    --page: #ffffff;
    --band-dark: #2f2f2f;
    --orange: #d8730f;
    --orange-deep: #c4620a;
    --orange-text: #c8711c;
    --nav-bg: #f1f1f1;
    --nav-edge: #cfcfcf;
    --nav-text: #4a4a4a;
    --body-text: #3a3a3a;
    --social-blue: #3b5998;
    --footer: #343434;
    --footer-text: #e8e8e8;
    --frame: #f7f7f7;
  }
  * { box-sizing: border-box; margin: 0; padding: 0; }
  html, body {
    width: 1200px; height: 900px; overflow: hidden;
    background: var(--canvas);
  }
  .page {
    position: absolute; left: 55px; top: 108px;
    width: 1091px; height: 682px;
    background: var(--page);
    overflow: hidden;
    box-shadow: 0 0 2px rgba(0,0,0,.15);
  }
  .top-band {
    position: absolute; left: 0; top: 0; width: 100%; height: 50px;
    background: linear-gradient(90deg, #bdbdbd 0%, #8a8a8a 20%, var(--band-dark) 30%, var(--band-dark) 62%, #9a9a9a 75%, #d4d4d4 100%);
  }
  .header-photo {
    position: absolute; left: 33px; top: 68px; width: 336px; height: 211px;
    background: radial-gradient(ellipse at 55% 40%, #a2521d 0%, #7a3a14 30%, #efe6cf 55%, #fbf7ee 100%);
  }
  .banner {
    position: absolute; left: 430px; top: 50px; width: 661px; height: 205px;
  }
  .brand {
    position: absolute; left: 535px; top: 68px;
    display: flex; align-items: center; gap: 24px;
    color: #fff;
    font-family: "Noto Sans TC", sans-serif;
    font-weight: 400;
  }
  .brand-mark {
    width: 78px; height: 78px; border-radius: 50%;
    background: var(--orange-deep);
    flex: none;
  }
  .brand-name { font-size: 31px; line-height: 1.2; letter-spacing: 1px; }
  .brand-slogan { font-size: 41px; line-height: 1.3; letter-spacing: 1px; }
  .nav-ribbon {
    position: absolute; left: 537px; top: 203px; width: 540px; height: 62px;
  }
  .main-nav {
    position: absolute; left: 563px; top: 228px;
    display: flex; list-style: none;
    font-family: "Arimo", sans-serif; font-weight: 700; font-size: 14px;
    color: var(--nav-text);
  }
  .main-nav li { margin-right: 0; }
  .main-nav li:nth-child(1) { width: 97px; }
  .main-nav li:nth-child(2) { width: 110px; }
  .main-nav li:nth-child(3) { width: 96px; }
  .main-nav li:nth-child(4) { width: 97px; }
  .photo-back {
    position: absolute; left: 236px; top: 363px; width: 150px; height: 245px;
    background: var(--frame); border: 1px solid #d6d6d6; border-radius: 6px;
    padding: 7px; transform: rotate(4deg);
    box-shadow: 0 2px 4px rgba(0,0,0,.15);
  }
  .photo-front {
    position: absolute; left: 53px; top: 329px; width: 183px; height: 254px;
    background: var(--frame); border: 1px solid #d0d0d0; border-radius: 8px;
    padding: 8px; box-shadow: 0 2px 5px rgba(0,0,0,.2);
  }
  .photo-fill { width: 100%; height: 100%; }
  .photo-back .photo-fill { background: linear-gradient(160deg, #f2f2f2 0%, #b5651f 45%, #6d3210 80%, #2a1a10 100%); }
  .photo-front .photo-fill { background: linear-gradient(170deg, #8c8378 0%, #b02a2a 45%, #5a2c25 70%, #d9d4cc 100%); }
  .content {
    position: absolute; left: 451px; top: 328px; width: 410px;
    font-family: "Roboto Condensed", sans-serif;
    color: var(--body-text);
  }
  .content h1 {
    font-weight: 300; font-size: 30px; color: var(--orange-text);
    line-height: 1; margin-bottom: 17px;
  }
  .content p { font-size: 13px; line-height: 17px; font-weight: 400; }
  .content h2 {
    font-weight: 400; font-size: 13px; color: var(--orange-text);
    margin: 20px 0 3px;
  }
  .like-box {
    position: absolute; left: 879px; top: 341px;
    display: flex; gap: 8px;
    font-family: "Arimo", sans-serif;
  }
  .like-box-mark { width: 40px; height: 40px; background: var(--social-blue); flex: none; }
  .like-box-title { font-size: 13px; font-weight: 700; color: var(--social-blue); }
  .like-box-row { display: flex; align-items: center; gap: 12px; margin-top: 5px; font-size: 10px; color: #555; }
  .like-button {
    border: 1px solid #c3c8d4; background: #eceef5; color: var(--social-blue);
    font-size: 10px; padding: 2px 6px;
  }
  .note-decoration {
    position: absolute; left: 882px; top: 531px; width: 170px; height: 97px;
    background: radial-gradient(ellipse at 40% 55%, #c9c9c9 0%, #e4e4e4 45%, rgba(255,255,255,0) 75%);
  }
  .footer {
    position: absolute; left: 0; bottom: 0; width: 100%; height: 42px;
    background: var(--footer);
    font-family: "Arimo", sans-serif; font-size: 11px; color: var(--footer-text);
    padding: 14px 0 0 40px; letter-spacing: .3px;
  }
</style>
</head>
<body>
  <div class="page">
    <div class="top-band" role="img" aria-label="Sheet music and piano keys in black and white"></div>

    <div class="header-photo" role="img" aria-label="Violin and bow resting on sheet music"></div>

    <svg class="banner" viewBox="0 0 661 205" aria-hidden="true">
      <defs>
        <linearGradient id="bannerFill" x1="0" y1="0" x2="0" y2="1">
          <stop offset="0" stop-color="#e07c18"/>
          <stop offset="1" stop-color="#cf6a0c"/>
        </linearGradient>
      </defs>
      <path d="M74 0 H661 V205 H74 V130 C60 128 56 124 56 114 V80 C56 70 60 66 74 64 Z" fill="url(#bannerFill)"/>
    </svg>

    <div class="brand">
      <span class="brand-mark"></span>
      <div>
        <div class="brand-name">悅聲藝術</div>
        <div class="brand-slogan">用音樂愉悅您的賓客</div>
      </div>
    </div>

    <svg class="nav-ribbon" viewBox="0 0 540 62" aria-hidden="true">
      <defs>
        <linearGradient id="navFill" x1="0" y1="0" x2="0" y2="1">
          <stop offset="0" stop-color="#fafafa"/>
          <stop offset="1" stop-color="#e2e2e2"/>
        </linearGradient>
      </defs>
      <path d="M480 0 L513 6 L522 62 L500 46 Z" fill="#bdbdbd"/>
      <path d="M12 6 L48 0 L498 0 L506 46 L0 52 Z" fill="url(#navFill)" stroke="var(--nav-edge)" stroke-width="1"/>
    </svg>

    <ul class="main-nav">
      <li>Groups</li>
      <li>Members</li>
      <li>Videos</li>
      <li>Pricing</li>
      <li>Order</li>
    </ul>

    <div class="photo-back">
      <div class="photo-fill" role="img" aria-label="Close-up of a violin body"></div>
    </div>
    <div class="photo-front">
      <div class="photo-fill" role="img" aria-label="Three musicians in evening gowns with piano, violin and trombone"></div>
    </div>

    <div class="content">
      <h1>Wedding music</h1>
      <p>Cras neque justo, ultrices at, rhoncus a facilisis eget,nisl. Quisque vitae pede. Nam et augue. Sed a elit. Ut vel massa. Suspendisse nibh pede, ultrices vitae ultrices nec, mollis no nibh. In sit amet pede quis leo vulputate hendrerit.</p>
      <h2>CRAS NEQUE JUSTO</h2>
      <p>Cras neque justo, ultrices at, rhoncus a facilisis eget,nisl. Quisque vitae pede. Nam et augue. Sed a elit. Ut vel massa. Suspendisse nibh pede, ultrices vitae ultrices nec, mollis no nibh. In sit amet pede quis leo vulputate hendrerit. Cras aoreet leo et justo auctor condimentum. Quisque vitae pede. Nam et augue. Sed a elit. Ut vel massa. In sit amet pede quis leo vulputate hendrerit. Cras aoreet leo et justo auctor condimentum.</p>
    </div>

    <div class="like-box">
      <span class="like-box-mark"></span>
      <div>
        <div class="like-box-title">Chatterly Platform</div>
        <div class="like-box-row">
          <span class="like-button">Like</span>
          <span>2,721,759</span>
        </div>
      </div>
    </div>

    <div class="note-decoration" role="img" aria-label="Faint treble clef and music notes on a curling staff"></div>

    <div class="footer">Copyright 2011. All rights reserved.</div>
  </div>
</body>
</html>
```